New "above the fold" design for our website

We would like to see some new creative designs for our above the fold section on our homepage. We are an online marketplace for fresh produce and meat.

You must design the desktop and mobile layouts.

Target Market(s)

Women 30-45 years old who buy groceries, with 2 children under 10 years old.

Industry/Entity Type

Grocery Store

Number of Pages Required

1 page

Font styles to use
Sans Serif

Requirements
Must have
• Give customers the sense of organic and farm fresh as we are battling the big supermarket chains.
Nice to have
• Pictures of produce. Pictures of farmers.

```html
<!DOCTYPE html>
<html lang="en">
<head>
<meta charset="utf-8">
<title>Fieldhand — Quality Meat &amp; Produce</title>
<link rel="stylesheet" href="https://fonts.googleapis.com/css2?family=Ubuntu:wght@300;400;500;700&family=Open+Sans:wght@700;800&display=swap">
<style>
  :root {
    --olive: #5a6b24;
    --olive-border: #8a9b45;
    --forest: #1f4410;
    --green-btn: #58962c;
    --green-btn-dark: #47801f;
    --cream: #f6efe6;
    --beige: #e6ddcf;
    --text: #4a4a4a;
    --heading-dark: #2a2a2a;
    --footer-bg: #262628;
    --footer-text: #c9c9c9;
    --link-green: #a9c25a;
    --hero-top: #6f9fae;
    --hero-bottom: #5c8f3c;
    --placeholder-light: #d8d6cf;
    --placeholder-soft: #e4e2dd;
    --white: #ffffff;
  }
  * { box-sizing: border-box; margin: 0; padding: 0; }
  html, body { width: 1200px; height: 1072px; overflow: hidden; }
  body { font-family: "Ubuntu", sans-serif; background: var(--white); color: var(--text); position: relative; }

  .hero { position: absolute; left: 0; top: 0; width: 1200px; height: 543px; overflow: hidden; }
  .hero-photo {
    position: absolute; inset: 0;
    background: linear-gradient(180deg, var(--hero-top), var(--hero-bottom));
  }
  .hero-person {
    position: absolute; left: 857px; top: 206px; width: 343px; height: 337px;
    background: var(--placeholder-light);
  }

  .logo {
    position: absolute; left: 99px; top: 26px; width: 205px; height: 109px;
    background: var(--olive); border: 3px solid var(--olive-border); border-radius: 18px;
    display: flex; align-items: center; justify-content: center;
    color: var(--white); font-size: 23px; font-weight: 500; letter-spacing: 1.5px;
  }

  .nav { position: absolute; top: 66px; left: 556px; display: flex; align-items: center; }
  .nav a { color: var(--white); text-decoration: none; font-size: 14px; font-weight: 700; letter-spacing: 0.5px; }
  .nav .nav-link { margin-right: 58px; }
  .nav .nav-login {
    background: var(--olive); border: 2px solid var(--olive-border); border-radius: 8px;
    padding: 9px 16px; margin-left: -5px; margin-right: 55px;
  }

  .hero-title { position: absolute; left: 99px; top: 226px; color: var(--white); font-family: "Open Sans", sans-serif; font-weight: 800; font-size: 40px; letter-spacing: 0.3px; white-space: nowrap; }
  .hero-sub { position: absolute; left: 99px; top: 284px; color: var(--white); font-size: 28px; font-weight: 400; white-space: nowrap; }

  .btn { position: absolute; top: 344px; width: 222px; height: 47px; display: flex; align-items: center; justify-content: center; font-size: 20px; font-weight: 700; border-radius: 2px; }
  .btn-year { left: 99px; background: var(--cream); color: var(--heading-dark); }
  .btn-shop { left: 340px; background: linear-gradient(180deg, var(--green-btn), var(--green-btn-dark)); color: var(--white); letter-spacing: 0.5px; }

  .stats { position: absolute; left: 97px; top: 441px; display: flex; align-items: center; color: var(--white); font-size: 15px; white-space: nowrap; }
  .stat { display: flex; align-items: center; margin-right: 17px; }
  .stat svg { margin-right: 12px; }

  .about { position: absolute; left: 99px; top: 582px; width: 640px; }
  .about h2 { font-weight: 400; font-size: 25px; color: var(--olive); letter-spacing: 0.3px; white-space: nowrap; }
  .about h3 { font-weight: 400; font-size: 18px; color: var(--heading-dark); margin-top: 12px; white-space: nowrap; }
  .about p { font-size: 12.5px; line-height: 24px; margin-top: 14px; }
  .about p + p { margin-top: 16px; }
  .btn-more {
    display: inline-block; margin-top: 20px; background: var(--olive); color: var(--white);
    font-size: 14px; font-weight: 500; padding: 10px 17px; box-shadow: 2px 2px 0 #b7bf9a;
  }

  .steps { position: absolute; left: 788px; top: 670px; }
  .step { width: 45px; height: 45px; border-radius: 50%; display: flex; align-items: center; justify-content: center; font-size: 19px; margin-bottom: 20px; background: var(--beige); color: var(--olive); }
  .step.active { background: var(--forest); color: var(--white); }

  .team-photo {
    position: absolute; left: 900px; top: 568px; width: 193px; height: 410px;
    background: var(--placeholder-soft);
  }

  .footer { position: absolute; left: 0; top: 978px; width: 1200px; height: 94px; background: var(--footer-bg); color: var(--footer-text); }
  .footer-nav { position: absolute; left: 101px; top: 23px; font-size: 14px; }
  .footer-nav a { color: var(--footer-text); text-decoration: none; }
  .footer-nav span { margin: 0 8px; }
  .copyright { position: absolute; left: 101px; top: 58px; font-size: 12.5px; }
  .copyright a { color: var(--link-green); }
  .social { position: absolute; left: 1013px; top: 35px; display: flex; }
  .social span { width: 25px; height: 25px; border-radius: 50%; background: #8a8a8a; margin-right: 6px; }
  .social span:first-child { background: var(--olive); }
</style>
</head>
<body>
  <header class="hero">
    <div class="hero-photo" role="img" aria-label="Cows grazing on a green pasture under a blue sky"></div>
    <div class="hero-person" role="img" aria-label="Smiling butcher in a white apron holding a tray of raw meat"></div>

    <div class="logo">FIELDHAND</div>

    <nav class="nav">
      <a class="nav-link" href="#">HOW IT WORKS</a>
      <a class="nav-link" href="#">ABOUT</a>
      <a class="nav-link" href="#">REGISTER</a>
      <a class="nav-login" href="#">LOGIN</a>
      <svg width="14" height="14" viewBox="0 0 14 14" aria-label="Search"><circle cx="5.5" cy="5.5" r="4.2" fill="none" stroke="#fff" stroke-width="2"/><line x1="8.6" y1="8.6" x2="12.5" y2="12.5" stroke="#fff" stroke-width="2.2" stroke-linecap="round"/></svg>
    </nav>

    <svg style="position:absolute;left:32px;top:252px" width="24" height="40" viewBox="0 0 24 40"><polyline points="20,2 3,20 20,38" fill="none" stroke="rgba(255,255,255,0.7)" stroke-width="2"/></svg>

    <h1 class="hero-title">QUALITY MEAT &amp; PRODUCE</h1>
    <p class="hero-sub">DELIVERED TO YOUR DOOR</p>

    <div class="btn btn-year">2016</div>
    <div class="btn btn-shop">SHOP NOW</div>

    <div class="stats">
      <div class="stat">
        <svg width="42" height="42" viewBox="0 0 42 42"><circle cx="21" cy="21" r="19" fill="var(--cream)" stroke="#c9c38a" stroke-width="3"/><rect x="16" y="13" width="10" height="16" fill="none" stroke="var(--olive)" stroke-width="1.6"/><line x1="18.5" y1="17" x2="23.5" y2="17" stroke="var(--olive)" stroke-width="1.4"/><line x1="18.5" y1="21" x2="23.5" y2="21" stroke="var(--olive)" stroke-width="1.4"/><line x1="18.5" y1="25" x2="23.5" y2="25" stroke="var(--olive)" stroke-width="1.4"/></svg>
        34482 Orders
      </div>
      <div class="stat">
        <svg width="42" height="42" viewBox="0 0 42 42"><circle cx="21" cy="21" r="19" fill="none" stroke="#fff" stroke-width="3"/><circle cx="21" cy="18" r="3.2" fill="#fff"/><circle cx="14.5" cy="19" r="2.5" fill="#fff"/><circle cx="27.5" cy="19" r="2.5" fill="#fff"/><path d="M15 27c0-3.5 2.7-5 6-5s6 1.5 6 5z" fill="#fff"/></svg>
        10088 Customers
      </div>
      <div class="stat">
        <svg width="42" height="42" viewBox="0 0 42 42"><circle cx="21" cy="21" r="19" fill="none" stroke="#fff" stroke-width="3"/><path d="M14 20h4v9h-4zM18 20l4-7c2 0 2 2 1.5 4H29v3l-2 6h-9" fill="none" stroke="#fff" stroke-width="1.6" stroke-linejoin="round"/></svg>
        10279 Linkes
      </div>
      <div class="stat">
        <svg width="42" height="42" viewBox="0 0 42 42"><circle cx="21" cy="21" r="19" fill="none" stroke="#fff" stroke-width="3"/><circle cx="21" cy="21" r="5" fill="#fff"/></svg>
        4406 Social Followers
      </div>
    </div>
  </header>

  <section class="about">
    <h2>ON THE OTHER HAND, WE DENOUNCE WITH RIGHTEOUS</h2>
    <h3>At vero eos et accusamus et iusto odio dignissimos ducimus</h3>
    <p>On the other hand, we denounce with righteous indignation and dislike men who are so beguiled and demoral­ized by the charms of pleasure of the moment, so blinded by desire, that they cannot foresee the pain and trouble that are bound to ensue; and equal blame belongs to those who fail in their duty through weakness of will, which is the same as saying through shrinking from toil and pain. These cases are perfectly simple and easy to distinguish. In</p>
    <p>In a free hour, when our power of choice is untrammelled and when nothing prevents our being able to do what we like best, every pleasure is to be welcomed and every pain avoided. But in certain circumstances and owing to the claims of duty or the obligations of business it will frequently occur that pleasures have to be repudiated and annoyances</p>
    <span class="btn-more">READ MORE</span>
  </section>

  <div class="steps">
    <div class="step active">1</div>
    <div class="step">2</div>
    <div class="step">3</div>
  </div>

  <div class="team-photo" role="img" aria-label="Butcher in a striped navy apron standing with arms crossed"></div>

  <footer class="footer">
    <nav class="footer-nav">
      <a href="#">Home</a><span>/</span><a href="#">About Us</a><span>/</span><a href="#">Blog</a><span>/</span><a href="#">Services</a><span>/</span><a href="#">Contact Us</a>
    </nav>
    <p class="copyright">Copyright 2016 © <a href="#">Fieldhand</a>. All rights reserved</p>
    <div class="social" aria-label="Social links"><span></span><span></span><span></span></div>
  </footer>
</body>
</html>
```